Need a professional appearance with as much information about the company as possible without being to much (if that makes sense). We are a ambulance company. Would like our list of services on the back (which i can email later, theres about ) along with our legal business name (Harlow TransCare LLC). Ive attached our logo that was designed for us 6 years ago. would like for the star of life to be have the metallic appearance. These are just my ideas, I'm not a professional designer so am open to all ideas.

```html
<!DOCTYPE html>
<html lang="en">
<head>
<meta charset="utf-8">
<title>Harlow TransCare LLC – Business Card</title>
<link href="https://fonts.googleapis.com/css2?family=Open+Sans:wght@400;600;700;800&display=swap" rel="stylesheet">
<style>
  :root {
    --page-bg: #e4e5e7;
    --card-top: #55585d;
    --card-bottom: #2c2e31;
    --brand-blue: #1b7bc8;
    --text-white: #ffffff;
    --text-soft: #e9ebee;
    --card-w: 540px;
    --card-h: 309px;
  }
  * { box-sizing: border-box; margin: 0; padding: 0; }
  html, body {
    width: 1200px; height: 947px; overflow: hidden;
    background: var(--page-bg);
    font-family: "Open Sans", Arial, sans-serif;
  }
  .sheet {
    width: 1200px; height: 947px;
    display: flex; align-items: center; justify-content: center; gap: 40px;
  }
  .card {
    width: var(--card-w); height: var(--card-h);
    background: linear-gradient(160deg, var(--card-top), var(--card-bottom));
    color: var(--text-white);
    position: relative;
    box-shadow: 0 6px 18px rgba(0,0,0,.18);
  }

  /* ---------- Front: name + contact ---------- */
  .brand {
    position: absolute; top: 40px; right: 34px;
    display: flex; align-items: center; gap: 10px;
  }
  .brand-square { width: 18px; height: 18px; background: var(--brand-blue); }
  .brand-name {
    font-size: 34px; font-weight: 700; letter-spacing: .5px;
    color: var(--text-white);
  }
  .contact {
    position: absolute; left: 30px; top: 130px;
    list-style: none; font-size: 13px; line-height: 1.45; color: var(--text-soft);
  }
  .contact li { display: flex; align-items: center; gap: 10px; margin-bottom: 3px; }
  .contact .icon { width: 14px; height: 14px; flex: none; fill: var(--brand-blue); }
  .contact .fax { display: inline-flex; align-items: center; gap: 8px; margin-left: 16px; }

  /* ---------- Back: services ---------- */
  .services-title {
    text-align: center; font-weight: 800; font-size: 19px; letter-spacing: .5px;
    padding-top: 14px; height: 46px;
  }
  .services-core {
    background: var(--brand-blue);
    display: grid; grid-template-columns: 1fr 1fr;
    padding: 6px 34px; font-size: 15px; font-weight: 600; line-height: 1.3;
  }
  .services-core ul { list-style: none; }
  .bullet { color: var(--text-white); margin-right: 6px; font-weight: 400; }
  .services-list {
    padding: 8px 30px 0; font-size: 14px; line-height: 1.42; color: var(--text-soft);
  }
  .services-list .bullet { margin: 0 6px 0 8px; color: #9cc8ee; }
  .services-list p:first-child .bullet:first-child { margin-left: 0; }
  .hours {
    position: absolute; left: 26px; right: 26px; bottom: 16px;
    border: 2px solid var(--brand-blue); border-radius: 10px;
    text-align: center; font-weight: 800; font-size: 19px; padding: 4px 0;
    letter-spacing: .4px;
  }
</style>
</head>
<body>
<main class="sheet">

  <section class="card card-front" aria-label="Card front">
    <div class="brand">
      <span class="brand-square"></span>
      <span class="brand-name">Harlow TransCare</span>
    </div>
    <ul class="contact">
      <li>
        <svg class="icon" viewBox="0 0 14 14"><path d="M7 0a5 5 0 0 0-5 5c0 3.7 5 9 5 9s5-5.3 5-9a5 5 0 0 0-5-5zm0 7a2 2 0 1 1 0-4 2 2 0 0 1 0 4z"/></svg>
        <span>Physical Address : 418 Ridgeview Avenue Halden, GA 30599</span>
      </li>
      <li>
        <span class="icon"></span>
        <span>Mailing Address : P.O. Box 4172 Halden, GA 30598</span>
      </li>
      <li>
        <svg class="icon" viewBox="0 0 14 14"><path d="M3 1l2 0 1 3-1.5 1.2a8 8 0 0 0 4.3 4.3L10 8l3 1v2c0 1-1 2-2 2A11 11 0 0 1 1 3c0-1 1-2 2-2z"/></svg>
        <span>555.014.2601</span>
        <span class="fax">
          <svg class="icon" viewBox="0 0 14 14"><path d="M3 0h8v4H3zM1 5h12v6h-2v3H3v-3H1zm3 4v4h6V9z"/></svg>
          555.014.2602
        </span>
      </li>
      <li>
        <svg class="icon" viewBox="0 0 14 14"><path d="M0 3h14v8H0zm1 1v.3l6 4 6-4V4z"/></svg>
        <span>info@harlowtranscare.com</span>
      </li>
      <li>
        <svg class="icon" viewBox="0 0 14 14"><path d="M7 0a7 7 0 1 0 0 14A7 7 0 0 0 7 0zm5.9 6.3h-2.6a11 11 0 0 0-1-4.8 6 6 0 0 1 3.6 4.8zM7 1.2c.7 1 1.3 2.9 1.4 5.1H5.6C5.7 4.1 6.3 2.2 7 1.2zM4.7 1.5a11 11 0 0 0-1 4.8H1.1a6 6 0 0 1 3.6-4.8zM1.1 7.7h2.6a11 11 0 0 0 1 4.8 6 6 0 0 1-3.6-4.8zM7 12.8c-.7-1-1.3-2.9-1.4-5.1h2.8c-.1 2.2-.7 4.1-1.4 5.1zm2.3-.3a11 11 0 0 0 1-4.8h2.6a6 6 0 0 1-3.6 4.8z"/></svg>
        <span>www.harlowtranscare.com</span>
      </li>
    </ul>
  </section>

  <section class="card card-back" aria-label="Card back">
    <h2 class="services-title">SERVICES PROVIDED:</h2>
    <div class="services-core">
      <ul>
        <li><span class="bullet">»</span>Advanced Life Support</li>
        <li><span class="bullet">»</span>Basic Life Support</li>
        <li><span class="bullet">»</span>Bariatric (1600lbs)</li>
      </ul>
      <ul>
        <li><span class="bullet">»</span>NET Wheel Chair / Stretcher</li>
        <li><span class="bullet">»</span>Special Event Standby</li>
        <li><span class="bullet">»</span>CPR / First Aid Training</li>
      </ul>
    </div>
    <div class="services-list">
      <p><span class="bullet">»</span>Hospital Transfers<span class="bullet">»</span>Dialysis<span class="bullet">»</span>Wound Care<span class="bullet">»</span>Chemotherapy</p>
      <p><span class="bullet">»</span>Infusion<span class="bullet">»</span>Radiation<span class="bullet">»</span>Imaging Services<span class="bullet">»</span>Surgical Procedures</p>
      <p><span class="bullet">»</span>Emergency Room Transfers<span class="bullet">»</span>Hospital &amp; Nursing Home Discharges</p>
      <p><span class="bullet">»</span>Bariatric<span class="bullet">»</span>Doctors Appointments<span class="bullet">»</span>Direct Admits</p>
      <p><span class="bullet">»</span>Hospice<span class="bullet">»</span>Long Distance<span class="bullet">»</span>Wheel Chair</p>
    </div>
    <div class="hours">SERVICES AVAILABLE 24 HOURS A DAY</div>
  </section>

</main>
</body>
</html>
```